Business Card Upgrade

I have designed our business card using our new logo. I think it needs imporovements. We used to have two cards for our business. One card was for our software business, and the other was for our consulting business. We are now in the process of combining our websites, marketing, name, and a new logo.

Our goal is to have a really sharp professional logo. One reason I designed the card the way I did was that our Titles are sometimes long, and by separating the person's name and title, it shows up very well and the title can be adjusted no matter how long it is. Sometimes the title can be 4 or 5 words or more.

We really like our logo on black as it shows up very nice. Our PMS colors are as follows: 368C and 459C.

The Designer that will be working with us will need to deliver the following:

The front and back of the Business Card Design will need to be delivered in a high quality JPEG, and
The front and back of the Business Card Design in Illustrator Format .ai
Any fonts will need to be sent to us if they are not standard and are required to open the Illustrator file correctly.

To help us get a good idea of the card with a title, please use the title: " Director of Software Development "

NOTE: The chosen designer will be selected to design our new letterhead within 2 weeks from the closing of this contest.

To help us make sure the card design works with longer titles, please use the followign job title on the card:  

"Director of Software and Product Development"

 

ALL DESIGNERS:

1. I appreciate the different angles you are showing the cards, but please be sure and always show the direct view, so I can see the layout and what the person I hand the card will see.

2. Please do not use white.  Please use off white as I don't care for white cards and they get dirty easy and do not represent the designs well.

Dear Designers,

Please provide samples straight one as a viewer of the card will see.  Some of the angles that are presented make it impossible to tell how everything fits, and sometimes even makes areas look skewed. So, please provide a straight sample view.

Pinnacle 400 company executives such as Vice Presidents, and Directors

Software

• Professional looking Card.

Our customers are Directors, Vice Presidents, and Presidents of companies as large as Pinnacle 400 companies. The card needs to get attention wile still looking professional.

Delivery of the finished product in Illustrator Format with any fonts needed to edit the text or open the file.

The card will be a heavy stock with a soft touch coating for that silk feel.

```html
<!DOCTYPE html>
<html lang="en">
<head>
<meta charset="utf-8">
<title>Harborline Business Card – Front and Back</title>
<link rel="stylesheet" href="https://fonts.googleapis.com/css2?family=Bebas+Neue&family=Montserrat:wght@300&display=swap">
<style>
  :root {
    --page: #ffffff;
    --card-dark: #1b1919;
    --card-mid: #2a2727;
    --card-glow: #3a3737;
    --brand-green: #4fb23f;
    --brand-gold: #ecd99a;
    --back-light: #7a7878;
  }
  * { margin: 0; padding: 0; box-sizing: border-box; }
  html, body {
    width: 1200px;
    height: 900px;
    overflow: hidden;
    background: var(--page);
  }
  .canvas {
    position: relative;
    width: 1200px;
    height: 900px;
  }
  .card {
    position: absolute;
    left: 398px;
    width: 416px;
    height: 236px;
    overflow: hidden;
  }
  .card--front {
    top: 179px;
    background:
      radial-gradient(ellipse 260px 200px at 95% 0%, var(--card-glow), transparent 70%),
      linear-gradient(180deg, var(--card-mid), var(--card-dark));
  }
  .card--back {
    top: 516px;
    background: var(--card-mid);
  }
  .front-texture {
    position: absolute;
    left: 0;
    top: 170px;
    width: 100%;
    height: 66px;
    background: linear-gradient(180deg, transparent, rgba(255, 255, 255, 0.04) 50%, transparent);
  }
  .back-glow {
    position: absolute;
    left: 0;
    top: 132px;
    width: 100%;
    height: 104px;
    background: radial-gradient(ellipse 75% 120% at 50% 100%, var(--back-light), var(--card-mid));
  }

  .brand-name {
    position: absolute;
    right: 18px;
    top: 24px;
    display: flex;
    align-items: center;
    gap: 8px;
    font-family: "Bebas Neue", sans-serif;
    font-size: 42px;
    letter-spacing: 3px;
    line-height: 1;
    color: var(--brand-green);
  }
  .brand-name__mark {
    width: 14px;
    height: 14px;
    background: var(--brand-green);
  }

  .person {
    position: absolute;
    left: 18px;
    top: 107px;
    font-family: "Bebas Neue", sans-serif;
  }
  .person__name {
    font-size: 23px;
    font-weight: 400;
    line-height: 1;
    color: var(--brand-green);
    letter-spacing: 0.3px;
  }
  .person__title {
    margin-top: 6px;
    font-size: 14px;
    line-height: 1;
    color: var(--brand-gold);
    letter-spacing: 0.2px;
  }
  .contact {
    position: absolute;
    left: 18px;
    top: 163px;
    font-family: "Bebas Neue", sans-serif;
    font-size: 12.5px;
    line-height: 16px;
    color: var(--brand-gold);
    letter-spacing: 0.2px;
    list-style: none;
  }

  .web-address {
    position: absolute;
    left: 0;
    right: 0;
    top: 106px;
    text-align: center;
    font-family: "Montserrat", sans-serif;
    font-weight: 300;
    font-size: 21px;
    letter-spacing: 1px;
    color: var(--brand-green);
    line-height: 1;
  }
</style>
</head>
<body>
<main class="canvas">

  <section class="card card--front" aria-label="Business card front">
    <div class="front-texture" role="img" aria-label="Soft decorative sheen along the lower edge"></div>

    <div class="brand-name">
      <span class="brand-name__mark"></span>
      <span>Harborline</span>
    </div>

    <div class="person">
      <h1 class="person__name">Dale Morrow</h1>
      <p class="person__title">Director of Software and Product Development</p>
    </div>

    <ul class="contact">
      <li>418 Cove Point Road</li>
      <li>Bayport, AL 36590</li>
      <li>251.555.0148 (Direct)</li>
      <li>dmorrow@harborlinecorp.com</li>
    </ul>
  </section>

  <section class="card card--back" aria-label="Business card back">
    <div class="back-glow" role="img" aria-label="Soft grey decorative glow along the lower edge"></div>
    <p class="web-address">WWW.HARBORLINE.COM</p>
  </section>

</main>
</body>
</html>
```